Poster to promote Global Critter Care Fest

Hi Designers,

Animal lovers all over the world are grateful for the work of vets.

To recognize all their efforts, Global Critter Care Fest takes place globally on April 30. This year's theme is 'Continuing education with a one health focus'.

It's about working alongside the human health sector to tackle animal disease and food safety. Read more here: http://www.kalvora.int/for-the-media/press-releases/detail/article/global-critter-care-fest-award-2016/

We want you to design a poster to promote the day, and the key message.

The poster must feature:
- the words 'Global Critter Care Fest'
- the date 'April 30, 2016'
- the theme 'Continuing education with a one health focus

You can choose any imagery and colors you feel will be engaging for the audience and will reflect the industry and messages.

Think animal, vets, pets, caring, health.

Looking forward to seeing your ideas.

Thanks

Pixelhive

Veterinary

• - the words 'Global Critter Care Fest'
• - the date 'April 30, 2016'
• - the theme 'Continuing education with a one health focus

```html
<!DOCTYPE html>
<html lang="en">
<head>
<meta charset="utf-8">
<title>Global Critter Care Fest 2016 Poster</title>
<link rel="stylesheet" href="https://fonts.googleapis.com/css2?family=Jost:wght@500;600&display=swap">
<style>
  :root {
    --stage: #e9e9e9;
    --poster-dark: #3a3a3c;
    --poster-mid: #5b5b5d;
    --headline: #ececec;
    --accent-red: #c0343a;
    --photo-light: #b9b9b9;
    --photo-dark: #2c2c2d;
  }
  * { margin: 0; padding: 0; box-sizing: border-box; }
  html, body {
    width: 1200px;
    height: 1200px;
    overflow: hidden;
    background: var(--stage);
  }
  .canvas {
    position: relative;
    width: 1200px;
    height: 1200px;
    display: flex;
    align-items: center;
    justify-content: center;
  }
  .poster {
    position: relative;
    width: 860px;
    height: 1080px;
    overflow: hidden;
    background: radial-gradient(ellipse at 70% 20%, var(--poster-mid) 0%, var(--poster-dark) 70%);
    box-shadow: 0 6px 24px rgba(0,0,0,0.18);
    font-family: "Jost", "Futura", sans-serif;
  }
  .poster__photo {
    position: absolute;
    left: 300px;
    top: 330px;
    width: 520px;
    height: 600px;
    border-radius: 46% 46% 12% 12% / 40% 40% 10% 10%;
    background: radial-gradient(ellipse at 45% 40%, var(--photo-light) 0%, #7d7d7e 45%, var(--photo-dark) 100%);
    opacity: 0.85;
  }
  .poster__date {
    position: absolute;
    left: 80px;
    top: 110px;
    color: var(--accent-red);
    font-weight: 500;
    font-size: 40px;
    letter-spacing: 4px;
  }
  .poster__title {
    position: absolute;
    left: 72px;
    top: 160px;
    color: var(--headline);
    font-weight: 600;
    text-transform: uppercase;
    line-height: 1;
    white-space: nowrap;
  }
  .poster__title-lead {
    display: block;
    font-size: 168px;
    letter-spacing: 2px;
  }
  .poster__title-line {
    display: block;
    font-size: 72px;
    letter-spacing: 5px;
    margin-top: 40px;
    padding-left: 60px;
  }
  .poster__title-line + .poster__title-line {
    margin-top: 12px;
  }
  .poster__theme {
    position: absolute;
    left: 80px;
    right: 80px;
    top: 970px;
    color: var(--headline);
    font-weight: 500;
    font-size: 30px;
    letter-spacing: 2px;
    line-height: 1.3;
    text-transform: uppercase;
  }
</style>
</head>
<body>
  <main class="canvas">
    <article class="poster">
      <div class="poster__photo" role="img" aria-label="Vintage black and white photograph of a puppy in a checked coat cuddling a tabby kitten"></div>
      <p class="poster__date">04.30.16</p>
      <h1 class="poster__title">
        <span class="poster__title-lead">Global</span>
        <span class="poster__title-line">Critter Care</span>
        <span class="poster__title-line">Fest 2016</span>
      </h1>
      <p class="poster__theme">Continuing education with a one health focus</p>
    </article>
  </main>
</body>
</html>
```